Tree Pruning Website

We need a website for a tree Arborist, pruning company called Hollow Ridge Groundcare. We look after all types of trees, knock down trees and prune trees. Our target market is from domestic clients to government clients and everything in between.

We would like to see the use of our main colours which are orange and green

We are not looking forward in seeing a template that we have seen before but a unique template. We have designed 5 templates ourselves and we wish for the design community to take our designs to the next level.

We have also designed a template for things that **we are not** looking for (Version 4)

To make it fair for everyone, we are also not giving out any participation payments as we have had. One winner will take all of the payment!!!

I Have attached a image of the designs and a image of a tree.

We are just looking at the PSD file been developed. We have our own team who can slice the image up into a HTML format.

Target Market(s)

Everyone who needs to cut down a tree

Industry/Entity Type

Government

Requirements
Must have
• Logo on front page
A List of our services
jQuery slider on page
Phone Number on every page

```html
<!DOCTYPE html>
<html lang="en">
<head>
<meta charset="utf-8">
<title>Hollow Ridge Groundcare</title>
<link href="https://fonts.googleapis.com/css2?family=Arimo:wght@400;700&display=swap" rel="stylesheet">
<style>
  :root {
    --sky-top: #8fc6ec;
    --sky-low: #dbeefa;
    --grass-light: #8cc63f;
    --grass: #5a9e26;
    --grass-deep: #4a9222;
    --brand-green: #3f8f1f;
    --heading-green: #3d8b22;
    --nav-brown: #5a3a1c;
    --nav-brown-dark: #3f2710;
    --nav-active: #3f961f;
    --search-tan: #c9a77a;
    --text: #333333;
    --panel-grey: #e6e6e6;
    --white: #ffffff;
  }
  * { margin: 0; padding: 0; box-sizing: border-box; }
  html, body { width: 1200px; height: 1000px; overflow: hidden; }
  body {
    position: relative;
    font-family: "Arimo", Arial, sans-serif;
    color: var(--text);
    background: var(--grass-deep);
  }
  .backdrop {
    position: absolute; inset: 0;
    background: linear-gradient(to bottom,
      var(--sky-top) 0px, var(--sky-low) 260px,
      #b9dca0 300px, var(--grass-light) 340px,
      var(--grass) 560px, var(--grass-deep) 760px, var(--grass-deep) 1000px);
  }
  .abs { position: absolute; }

  .brand { left: 470px; top: 52px; display: flex; align-items: center; gap: 10px; }
  .brand-mark { width: 30px; height: 30px; border-radius: 50%; background: var(--brand-green); }
  .brand-name { font-size: 22px; font-weight: 700; color: var(--brand-green); white-space: nowrap; }

  .call { right: 280px; top: 95px; text-align: left; }
  .call-label { font-size: 11px; color: #444; line-height: 13px; }
  .call-number { font-size: 16px; font-weight: 700; color: var(--nav-brown-dark); line-height: 20px; white-space: nowrap; }

  .main-nav {
    left: 281px; top: 130px; width: 639px; height: 39px; border-radius: 4px;
    background: linear-gradient(to bottom, var(--nav-brown), var(--nav-brown-dark));
  }
  .main-nav a {
    position: absolute; top: 0; height: 39px; line-height: 39px;
    color: var(--white); font-size: 13px; text-decoration: none; text-align: center;
  }
  .main-nav a.is-active { background: var(--nav-active); }
  .search {
    position: absolute; left: 499px; top: 10px; width: 131px; height: 20px;
    background: var(--search-tan); border: 1px solid #a88658;
    font-size: 8px; color: #4a3320; padding: 5px 5px; line-height: 10px;
  }
  .search svg { position: absolute; right: 4px; top: 4px; }

  .slider { left: 281px; top: 178px; width: 639px; height: 208px; background: var(--white); border-radius: 4px; box-shadow: 0 4px 10px rgba(0,0,0,.2); }
  .slide-photo { position: absolute; left: 5px; top: 5px; width: 630px; height: 198px; background: linear-gradient(135deg, #6a7f8e, #c8cdc4 45%, #7f8a6a); }
  .slide-panel { position: absolute; left: 5px; top: 5px; }
  .slide-title { left: 23px; top: 58px; font-size: 21px; font-weight: 700; color: var(--white); letter-spacing: .3px; }
  .slide-text { left: 24px; top: 89px; width: 215px; font-size: 9px; line-height: 14px; color: var(--white); }
  .read-more {
    left: 22px; top: 143px; width: 83px; height: 21px; line-height: 21px; text-align: center;
    background: linear-gradient(#ffffff, #dcdcdc); border-radius: 2px;
    font-size: 11px; font-weight: 700; color: var(--brand-green);
    box-shadow: 0 1px 2px rgba(0,0,0,.3);
  }
  .slider-dots { left: 565px; top: 399px; display: flex; gap: 3px; }
  .slider-dots span { width: 12px; height: 12px; border-radius: 50%; background: var(--brand-green); border: 1px solid #2b6a12; }

  .content { left: 281px; top: 421px; width: 639px; height: 455px; background: var(--white); border-radius: 4px; }
  .intro-title { left: 21px; top: 22px; font-size: 12.5px; font-weight: 700; color: var(--heading-green); }
  .intro-photo { left: 20px; top: 47px; width: 116px; height: 120px; background: linear-gradient(#5f8f3a, #2f5e1d); }
  .intro-text { left: 149px; top: 45px; width: 472px; font-size: 8.3px; line-height: 12.9px; color: var(--text); }
  .intro-text p + p { margin-top: 13px; }

  .feature { top: 189px; width: 186px; }
  .feature h2 { font-size: 15px; font-weight: 700; color: var(--heading-green); line-height: 18px; }
  .feature-photo { margin-top: 8px; height: 60px; }
  .feature-body { margin-top: 4px; height: 160px; background: var(--panel-grey); padding: 9px 9px; font-size: 8.3px; line-height: 12.6px; color: var(--text); }
  .feature-body p + p { margin-top: 13px; }

  .footer-note { left: 301px; top: 899px; font-size: 8.5px; color: var(--white); }
  .footer-links { right: 300px; top: 899px; font-size: 8.5px; color: var(--white); white-space: nowrap; }
  .footer-links .sep { margin: 0 8px; }
</style>
</head>
<body>
  <div class="backdrop" role="img" aria-label="Sky with clouds above a green meadow with trees and a park bench"></div>

  <header>
    <div class="brand abs"><span class="brand-mark"></span><span class="brand-name">Hollow Ridge Groundcare</span></div>
    <div class="call abs">
      <div class="call-label">Call Us Now</div>
      <div class="call-number">0800-555-01932</div>
    </div>
    <nav class="main-nav abs">
      <a class="is-active" href="#" style="left:8px;width:71px;">Home</a>
      <a href="#" style="left:92px;width:64px;">About Us</a>
      <a href="#" style="left:180px;width:88px;">Our Services</a>
      <a href="#" style="left:290px;width:90px;">Get a Quoute</a>
      <a href="#" style="left:405px;width:70px;">Contact Us</a>
      <div class="search">Search
        <svg width="12" height="12" viewBox="0 0 12 12"><circle cx="5" cy="5" r="3.3" fill="none" stroke="#4a3320" stroke-width="1.4"/><line x1="7.5" y1="7.5" x2="11" y2="11" stroke="#4a3320" stroke-width="1.6"/></svg>
      </div>
    </nav>
  </header>

  <section class="slider abs">
    <div class="slide-photo" role="img" aria-label="Looking up into pale tree trunks and green canopy"></div>
    <svg class="slide-panel" width="630" height="198" viewBox="0 0 630 198">
      <polygon points="0,0 275,0 222,198 0,198" fill="#3e8e20"/>
      <polygon points="75,0 110,0 58,198 23,198" fill="#ffffff" opacity=".08"/>
      <polygon points="140,0 175,0 123,198 88,198" fill="#ffffff" opacity=".08"/>
      <polygon points="205,0 240,0 188,198 153,198" fill="#ffffff" opacity=".08"/>
    </svg>
    <div class="slide-title abs">TREE PRUNING</div>
    <p class="slide-text abs">Lorem Ipsum is simply dummy text of the printing and typesetting industry. Lorem Ipsum has been the industry's standard dummy text ever since the 1500s,</p>
    <div class="read-more abs">READ MORE</div>
  </section>
  <div class="slider-dots abs"><span></span><span></span><span></span><span></span><span></span></div>

  <main class="content abs">
    <h1 class="intro-title abs">Lorem Ipsum is simply dummy text of the printing</h1>
    <div class="intro-photo abs" role="img" aria-label="Tall leafy tree in a grove"></div>
    <div class="intro-text abs">
      <p>Lorem Ipsum is simply dummy text of the printing and typesetting industry. Lorem Ipsum has been the industry's standard dummy text ever since the 1500s, when an unknown printer took a galley of type and scrambled it to make a type specimen book. It has survived not only five centuries, but also the leap into electronic typesetting, remaining essentially unchanged. It was popularised in the 1960s with the release of Typemark sheets containing Lorem Ipsum passages, and more recently with desktop publishing software like Foliant PageSetter including versions of Lorem Ipsum.</p>
      <p>Lorem Lorem Ipsum is simply dummy text of the printing and typesetting industry. Lorem Ipsum has been the industry's standard dummy text ever since the 1500s, Ipsum is simply dummy text of the printing and typesetting industry. Lorem Ipsum has been the industry's standard dummy text ever since the 1500s,</p>
    </div>

    <article class="feature abs" style="left:20px;">
      <h2>Who we are?</h2>
      <div class="feature-photo" role="img" aria-label="Arborist trimming branches" style="background:linear-gradient(90deg,#2f4a1e,#6e7a52);"></div>
      <div class="feature-body"><p>Lorem Ipsum is simply dummy text of the printing and typesetting industry. Lorem Ipsum has been the industry's standard dummy text ever since the 1500s, when an unknown printer took a galley of type and scrambled it to make a type specimen book. It has survived not only five centuries,</p><p>but also the leap into electronic typesetting, remaining essentially</p></div>
    </article>
    <article class="feature abs" style="left:226px;">
      <h2>Our Services</h2>
      <div class="feature-photo" role="img" aria-label="Climber working high in a tree against blue sky" style="background:linear-gradient(90deg,#7fb6e6,#c0723a 55%,#8fc0e8);"></div>
      <div class="feature-body"><p>Lorem Ipsum is simply dummy text of the printing and typesetting industry. Lorem Ipsum has been the industry's standard dummy text ever since the 1500s, when an unknown printer took a galley of type and scrambled it to make a type specimen book. It has survived not only five centuries,</p><p>but also the leap into electronic typesetting, remaining essentially</p></div>
    </article>
    <article class="feature abs" style="left:433px;">
      <h2>Why Hollow Ridge?</h2>
      <div class="feature-photo" role="img" aria-label="Twisted old tree trunk in a forest" style="background:linear-gradient(90deg,#5d6b3a,#6a4a34 50%,#7c8a5a);"></div>
      <div class="feature-body"><p>Lorem Ipsum is simply dummy text of the printing and typesetting industry. Lorem Ipsum has been the industry's standard dummy text ever since the 1500s, when an unknown printer took a galley of type and scrambled it to make a type specimen book. It has survived not only five centuries,</p><p>but also the leap into electronic typesetting, remaining essentially</p></div>
    </article>
  </main>

  <footer>
    <p class="footer-note abs">All right reserved Hollow Ridge Groundcare</p>
    <p class="footer-links abs">Copntact Us<span class="sep">I</span>Disclaimer<span class="sep">I</span>Privacy Policy</p>
  </footer>
</body>
</html>
```